Quarvex Power Point Template - Institutional Presentation

Develop a comprehensive template for a corporate presentation power point.

The presentation will be aimed to institutional investors.

Style to be modern and contemporary. Use of icons and images welcome but not to much.

It would be great if you could develop the layout/style for the content in the following slides:

- Cover
- Section title
- Slide with title and bullet points on one side and two text boxes on the other side
- Slide with line chart and pie chart
- Slide with table

Should we like the slides above we will then develop the rest of the template.

We may then need to have a dark-background version - but this will be invoiced separately.

Target Market(s)

Corporate institutional investors

Industry/Entity Type

Finance

Font styles to use
Serif
Sans Serif

Colors
3176b5
0255a3
cee9f5
86cae7
33a6d7
0792cd
33b8a4
00a990
86cfc6

Requirements
Must have
• Mostly white background with minimal objects
Nice to have
• Use of photos, but not to much.

```html
<!DOCTYPE html>
<html lang="en">
<head>
<meta charset="utf-8">
<title>Quarvex Corporate Overview Template</title>
<link href="https://fonts.googleapis.com/css2?family=Inter:wght@300;400;600;700&display=swap" rel="stylesheet">
<style>
:root{
  --canvas:#a9aaae;
  --navy:#2b3963;
  --navy-deep:#1f2b4f;
  --slate:#7e7f82;
  --grey-box:#a4a5a8;
  --ink:#2a2f45;
  --muted:#8a8b8f;
  --white:#ffffff;
  --rule:#d5d6da;
  --map-fill:#dcdee2;
}
*{box-sizing:border-box;margin:0;padding:0}
html,body{width:1200px;height:900px;overflow:hidden;background:var(--canvas);font-family:"Inter",Helvetica,Arial,sans-serif;color:var(--ink)}
.board{position:relative;width:1200px;height:900px}
.slide{position:absolute;width:289px;height:162px;background:var(--white);overflow:hidden}
.abs{position:absolute}
.c1{left:147px}.c2{left:440px}.c3{left:734px}
.r1{top:34px}.r2{top:202px}.r3{top:370px}.r4{top:537px}.r5{top:703px}

.brand{position:absolute;background:var(--navy);color:var(--white);font-weight:700;letter-spacing:2px;display:flex;align-items:center;justify-content:center}
.brand-lg{left:230px;top:5px;width:51px;height:13px;font-size:5.5px}
.brand-sm{left:254px;top:5px;width:27px;height:6px;font-size:3px;letter-spacing:1px}
.footer{position:absolute;left:0;bottom:0;width:100%;height:5px;background:var(--navy);color:var(--white);font-size:2.4px;display:flex;align-items:center;justify-content:space-between;padding:0 4px}

.head{position:absolute;left:17px;top:13px;border-left:0.8px solid var(--ink);padding-left:4px}
.head h2{font-size:7.5px;font-weight:400;letter-spacing:-0.2px;line-height:1}
.head p{font-size:4px;color:#555;margin-top:2px}
.on-dark .head{border-color:var(--white)}
.on-dark .head h2,.on-dark .head p{color:var(--white)}

.body{font-size:3.1px;line-height:1.55;color:#333;text-align:justify}
.body.light{color:var(--white)}
.photo{position:absolute}
.photo-dark{background:linear-gradient(135deg,#2d3b66 0%,#3d4d7a 55%,#25315a 100%)}
.bg-photo{position:absolute;inset:0;background:linear-gradient(120deg,#2a3862 0%,#41507c 50%,#2b3862 100%)}
.center{text-align:center}
</style>
</head>
<body>
<div class="board">

<!-- Cover -->
<section class="slide c1 r1 cover">
  <div class="brand brand-lg">QUARVEX</div>
  <div class="abs" style="left:24px;top:38px;height:18px;border-left:0.8px solid var(--ink)"></div>
  <div class="abs" style="left:31px;top:43px;font-size:6.5px;letter-spacing:-0.2px">CORPORATE&nbsp; OVERVIEW</div>
  <div class="abs" style="left:31px;top:51px;font-size:7px;color:var(--muted);font-weight:300">2015</div>
  <div class="photo" role="img" aria-label="Team of colleagues discussing around a glass board" style="left:0;top:64px;width:289px;height:72px;background:linear-gradient(90deg,#e9ecf1 0%,#c9d2de 35%,#b6c1cf 65%,#8f98a6 100%)"></div>
  <div class="abs" style="left:21px;top:148px;font-size:2.3px;color:#555">© 2017 All rights reserved. Contains confidential and proprietary information, not to be shared without prior consent of Quarvex.</div>
  <div class="abs" style="left:0;top:157px;width:289px;height:5px;background:var(--navy)"></div>
</section>

<!-- Table of contents -->
<section class="slide c2 r1 on-dark">
  <div class="bg-photo" role="img" aria-label="Navy toned office photo"></div>
  <div class="abs" style="left:28px;top:46px;font-size:3.5px;color:var(--white)">TABLE OF</div>
  <div class="abs" style="left:28px;top:52px;font-size:10px;color:var(--white);font-weight:300;letter-spacing:-0.3px">CONTENTS</div>
  <svg class="abs" style="left:0;top:0" width="289" height="162">
    <g font-family="Inter,sans-serif" font-size="3" font-weight="600">
      <g transform="translate(56,91)"><circle r="5.5" fill="#e4e5ea"/><text y="1" text-anchor="middle" fill="#2b3963">1</text><text x="12" y="-1" fill="#fff">LOREM IPSUM DOLOR SIT</text><text x="12" y="3" fill="#fff">MET DOLOR SIT MET</text></g>
      <g transform="translate(56,113)"><circle r="5.5" fill="#e4e5ea"/><text y="1" text-anchor="middle" fill="#2b3963">1</text><text x="12" y="-1" fill="#fff">LOREM IPSUM DOLOR SIT</text><text x="12" y="3" fill="#fff">MET DOLOR SIT MET</text></g>
      <g transform="translate(56,135)"><circle r="5.5" fill="#e4e5ea"/><text y="1" text-anchor="middle" fill="#2b3963">1</text><text x="12" y="-1" fill="#fff">LOREM IPSUM DOLOR SIT</text><text x="12" y="3" fill="#fff">MET DOLOR SIT MET</text></g>
      <g transform="translate(160,91)"><circle r="5.5" fill="#e4e5ea"/><text y="1" text-anchor="middle" fill="#2b3963">1</text><text x="12" y="-1" fill="#fff">LOREM IPSUM DOLOR SIT</text><text x="12" y="3" fill="#fff">MET DOLOR SIT MET</text></g>
      <g transform="translate(160,113)"><circle r="5.5" fill="#e4e5ea"/><text y="1" text-anchor="middle" fill="#2b3963">1</text><text x="12" y="-1" fill="#fff">LOREM IPSUM DOLOR SIT</text><text x="12" y="3" fill="#fff">MET DOLOR SIT MET</text></g>
      <g transform="translate(160,135)"><circle r="5.5" fill="#e4e5ea"/><text y="1" text-anchor="middle" fill="#2b3963">1</text><text x="12" y="-1" fill="#fff">LOREM IPSUM DOLOR SIT</text><text x="12" y="3" fill="#fff">MET DOLOR SIT MET</text></g>
    </g>
  </svg>
</section>

<!-- Vision & mission -->
<section class="slide c3 r1">
  <div class="photo photo-dark" role="img" aria-label="Navy toned photo of hands over documents" style="left:0;top:0;width:289px;height:89px"></div>
  <div class="abs" style="left:0;top:89px;width:289px;height:73px;background:var(--slate)"></div>
  <div class="abs" style="left:17px;top:14px;font-size:6.5px;color:var(--white);letter-spacing:-0.2px">VISION &amp; MISSION</div>
  <svg class="abs" style="left:0;top:0" width="289" height="162">
    <g fill="none" stroke="#fff">
      <circle cx="76" cy="85" r="13" fill="#2b3963" stroke-width="1.3"/>
      <circle cx="72" cy="86" r="3" stroke-width="1.4"/><circle cx="80" cy="86" r="3" stroke-width="1.4"/><path d="M75 85h2" stroke-width="1.2"/>
      <circle cx="198" cy="85" r="13" fill="#2b3963" stroke-width="1.3"/>
      <path d="M192 89a6 6 0 1 1 12 0" stroke-width="1.4"/><path d="M198 88l3-4" stroke-width="1.2"/>
    </g>
  </svg>
  <p class="abs center" style="left:30px;top:107px;width:94px;font-size:4px;line-height:1.3;color:var(--white)">To provide state of the art logistical and supply chain solutions to the defined needs of our customers using the best people, processes and systems in creating efficient and effective results.</p>
  <p class="abs center" style="left:151px;top:107px;width:94px;font-size:4px;line-height:1.3;color:var(--white)">To provide state of the art logistical and supply chain solutions to the defined needs of our customers using the best people, processes and systems in creating efficient and effective results.</p>
</section>

<!-- About us 1 -->
<section class="slide c1 r2">
  <div class="brand brand-sm">QUARVEX</div>
  <div class="head"><h2>ABOUT US</h2><p>SUBTITLE GOES HERE</p></div>
  <div class="abs" style="left:0;top:54px;width:94px;height:53px;background:var(--slate)"></div>
  <p class="abs" style="left:17px;top:71px;width:72px;font-size:3px;line-height:1.4;color:var(--white);font-weight:600">LOREM IPSUM DOLOR SIT MET CONSECTUR ADIPISCING ELIT, SED DO EIUSMOD TEMPOR INCIDIDUNT UT LABORE ET DOLORE MAGNA</p>
  <div class="photo" role="img" aria-label="Business people silhouetted against a bright window" style="left:93px;top:54px;width:196px;height:53px;background:linear-gradient(90deg,#dfe6ee,#b7c6d6 40%,#9fb3c8 70%,#dbe4ed)"></div>
  <p class="abs body" style="left:93px;top:115px;width:182px">Lorem ipsum dolor sit amet, consectetur adipiscing elit, sed do eiusmod tempor incididunt ut labore et dolore magna aliqua. Ut enim ad minim veniam, quis nostrud exercitation ullamco laboris nisi ut aliquip ex ea commodo consequat. Duis aute irure dolor in reprehenderit in voluptate velit esse cillum dolore eu fugiat nulla pariatur.</p>
  <div class="footer"><span>© 2017 All rights reserved</span><span>02</span></div>
</section>

<!-- About us 2 -->
<section class="slide c2 r2">
  <div class="brand brand-sm">QUARVEX</div>
  <div class="head"><h2>ABOUT US</h2><p>SUBTITLE GOES HERE</p></div>
  <div class="abs" style="left:106px;top:43px;width:183px;height:51px;background:var(--slate)"></div>
  <div class="photo" role="img" aria-label="Team gathered around a laptop in a meeting" style="left:10px;top:39px;width:96px;height:59px;background:linear-gradient(135deg,#c8d4e4,#5b74a6 50%,#2f3f6b)"></div>
  <p class="abs" style="left:116px;top:56px;width:160px;font-size:3px;line-height:1.6;color:var(--white);font-style:italic;font-weight:600">Lorem ipsum dolor sit amet, consectetur adipisicing elit, sed do eiusmod tempor incididunt ut labore et dolore magna aliqua. Ut enim ad minim veniam, quis nostrud exercitation ullamco laboris nisi ut aliquip ex ea commodo consequat. Duis aute irure dolor in reprehenderit in voluptate velit esse cillum dolore eu fugiat nulla pariatur.</p>
  <p class="abs body" style="left:116px;top:105px;width:162px">Lorem ipsum dolor sit amet, consectetur adipisicing elit, sed do eiusmod tempor incididunt ut labore et dolore magna aliqua. Ut enim ad minim veniam, quis nostrud exercitation ullamco laboris nisi ut aliquip ex ea commodo consequat. Duis aute irure dolor in reprehenderit in voluptate velit esse cillum dolore eu fugiat nulla pariatur. Excepteur sint occaecat cupidatat non proident, sunt in culpa qui officia deserunt mollit anim id est laborum.</p>
  <div class="footer"><span>© 2017 All rights reserved</span><span>02</span></div>
</section>

<!-- About us 3 -->
<section class="slide c3 r2">
  <div class="brand brand-sm">QUARVEX</div>
  <div class="head"><h2>ABOUT US</h2><p>SUBTITLE GOES HERE</p></div>
  <div class="photo" role="img" aria-label="Colleagues in suits reviewing a report" style="left:14px;top:44px;width:60px;height:38px;background:linear-gradient(135deg,#d3dbe6,#6d7fa3 55%,#2f3c63)"></div>
  <p class="abs center" style="left:20px;top:85px;width:52px;font-size:3px;line-height:1.4;color:var(--navy);font-weight:600">Lorem ipsum dolor sit amet consectetur adipisicing elit sed do eiusmod</p>
  <p class="abs body" style="left:86px;top:43px;width:90px">Lorem ipsum dolor sit amet, consectetur adipisicing elit, sed do eiusmod tempor incididunt ut labore et dolore magna aliqua. Ut enim ad minim veniam, quis nostrud exercitation ullamco laboris nisi ut aliquip ex ea commodo consequat. Duis aute irure dolor in reprehenderit in voluptate velit esse cillum dolore eu.</p>
  <p class="abs body" style="left:186px;top:43px;width:90px">Lorem ipsum dolor sit amet, consectetur adipisicing elit, sed do eiusmod tempor incididunt ut labore et dolore magna aliqua. Ut enim ad minim veniam, quis nostrud exercitation ullamco laboris nisi ut aliquip ex ea commodo consequat. Duis aute irure dolor in reprehenderit in voluptate velit esse cillum dolore eu.</p>
  <p class="abs body" style="left:86px;top:94px;width:90px">Lorem ipsum dolor sit amet, consectetur adipisicing elit, sed do eiusmod tempor incididunt ut labore et dolore magna aliqua. Ut enim ad minim veniam, quis nostrud exercitation ullamco laboris nisi ut aliquip ex ea commodo consequat. Duis aute irure dolor in reprehenderit in voluptate velit esse cillum dolore eu.</p>
  <p class="abs body" style="left:186px;top:94px;width:90px">Lorem ipsum dolor sit amet, consectetur adipisicing elit, sed do eiusmod tempor incididunt ut labore et dolore magna aliqua. Ut enim ad minim veniam, quis nostrud exercitation ullamco laboris nisi ut aliquip ex ea commodo consequat. Duis aute irure dolor in reprehenderit in voluptate velit esse cillum dolore eu.</p>
  <div class="footer"><span>© 2017 All rights reserved</span><span>02</span></div>
</section>

<!-- Our services dark -->
<section class="slide c1 r3 on-dark">
  <div class="bg-photo" role="img" aria-label="Navy toned photo of people walking in an office"></div>
  <div class="head"><h2>OUR SERVICES</h2><p>SUBTITLE GOES HERE</p></div>
  <svg class="abs" style="left:0;top:0" width="289" height="162">
    <g fill="#c9cdd8" stroke="#fff" stroke-width="1.2">
      <circle cx="50" cy="74" r="14"/><circle cx="142" cy="74" r="14"/><circle cx="234" cy="74" r="14"/>
    </g>
    <g fill="#fff">
      <rect x="45" y="68" width="9" height="11" rx="1"/><rect x="137" y="69" width="10" height="10" rx="2"/>
      <rect x="228" y="74" width="2" height="5"/><rect x="231" y="71" width="2" height="8"/><rect x="234" y="68" width="2" height="11"/><rect x="237" y="72" width="2" height="7"/>
    </g>
  </svg>
  <div class="abs center" style="left:10px;top:93px;width:80px;font-size:4.8px;color:var(--white);letter-spacing:-0.2px">LOREM IPSUM DOLOR</div>
  <div class="abs center" style="left:102px;top:93px;width:80px;font-size:4.8px;color:var(--white);letter-spacing:-0.2px">LOREM IPSUM DOLOR</div>
  <div class="abs center" style="left:194px;top:93px;width:80px;font-size:4.8px;color:var(--white);letter-spacing:-0.2px">LOREM IPSUM DOLOR</div>
  <p class="abs center" style="left:24px;top:106px;width:52px;font-size:3px;line-height:1.35;color:var(--white);font-weight:600">Dolor sit amet, consectetur adipisicing elit, sed do eiusmod tempor incididunt ut labore et dolore magna aliqua.</p>
  <p class="abs center" style="left:116px;top:106px;width:52px;font-size:3px;line-height:1.35;color:var(--white);font-weight:600">Dolor sit amet, consectetur adipisicing elit, sed do eiusmod tempor incididunt ut labore et dolore magna aliqua.</p>
  <p class="abs center" style="left:208px;top:106px;width:52px;font-size:3px;line-height:1.35;color:var(--white);font-weight:600">Dolor sit amet, consectetur adipisicing elit, sed do eiusmod tempor incididunt ut labore et dolore magna aliqua.</p>
</section>

<!-- About us services grid -->
<section class="slide c2 r3">
  <div class="brand brand-sm">QUARVEX</div>
  <div class="head"><h2>ABOUT US</h2><p>SUBTITLE GOES HERE</p></div>
  <svg class="abs" style="left:0;top:0" width="289" height="162" font-family="Inter,sans-serif">
    <g fill="#2b3963"><rect x="19" y="46" width="59" height="37"/><rect x="82" y="46" width="60" height="37"/><rect x="146" y="46" width="60" height="37"/><rect x="210" y="46" width="60" height="37"/></g>
    <g fill="#a4a5a8"><rect x="19" y="83" width="59" height="53"/><rect x="82" y="83" width="60" height="53"/><rect x="146" y="83" width="60" height="53"/><rect x="210" y="83" width="60" height="53"/></g>
    <g fill="none" stroke="#fff" stroke-width="1">
      <path d="M44 54l5-2 5 4-5 6-5-2z"/><circle cx="112" cy="59" r="5"/><path d="M112 57v5"/>
      <path d="M169 58l4-3 4 3 4-3 4 3-4 4-4-1-4 1z"/><circle cx="240" cy="59" r="1.5"/><circle cx="235" cy="55" r="1.2"/><circle cx="245" cy="55" r="1.2"/><circle cx="235" cy="63" r="1.2"/><circle cx="245" cy="63" r="1.2"/>
    </g>
    <g fill="#fff" font-size="3.3" text-anchor="middle" font-weight="600">
      <text x="48" y="73">MANAGEMENT</text><text x="48" y="77">SOLUTIONS</text>
      <text x="112" y="73">INFORMATION</text><text x="112" y="77">SOLUTIONS</text>
      <text x="176" y="73">PROFESSIONAL</text><text x="176" y="77">SERVICES</text>
      <text x="240" y="73">ORGANIZATIONAL</text><text x="240" y="77">TRANSFORMATION</text>
    </g>
  </svg>
  <p class="abs center" style="left:24px;top:89px;width:49px;font-size:2.8px;line-height:1.4;color:var(--white);font-weight:600">Dolor sit amet, consectetur adipisicing elit, sed do eiusmod tempor incididunt ut labore et dolore magna aliqua.</p>
  <p class="abs center" style="left:87px;top:89px;width:50px;font-size:2.8px;line-height:1.4;color:var(--white);font-weight:600">Dolor sit amet, consectetur adipisicing elit, sed do eiusmod tempor incididunt ut labore et dolore magna aliqua.</p>
  <p class="abs center" style="left:151px;top:89px;width:50px;font-size:2.8px;line-height:1.4;color:var(--white);font-weight:600">Dolor sit amet, consectetur adipisicing elit, sed do eiusmod tempor incididunt ut labore et dolore magna aliqua.</p>
  <p class="abs center" style="left:215px;top:89px;width:50px;font-size:2.8px;line-height:1.4;color:var(--white);font-weight:600">Dolor sit amet, consectetur adipisicing elit, sed do eiusmod tempor incididunt ut labore et dolore magna aliqua.</p>
  <div class="footer"><span>© 2017 All rights reserved</span><span>02</span></div>
</section>

<!-- About us partners -->
<section class="slide c3 r3">
  <div class="brand brand-sm">QUARVEX</div>
  <div class="head"><h2>ABOUT US</h2><p>SUBTITLE GOES HERE</p></div>
  <svg class="abs" style="left:0;top:0" width="289" height="162" role="img" aria-label="Grid of partner badges">
    <rect x="51" y="46" width="173" height="93" fill="#fff" stroke="#e3e4e7" stroke-width="0.6"/>
    <g fill="#c9ccd3">
      <rect x="67" y="55" width="26" height="9"/><rect x="111" y="55" width="26" height="9"/><rect x="155" y="55" width="26" height="9"/><rect x="199" y="55" width="12" height="12"/>
      <rect x="67" y="76" width="26" height="7"/><rect x="111" y="76" width="26" height="7"/><rect x="155" y="76" width="26" height="7"/><rect x="199" y="75" width="12" height="9"/>
      <rect x="67" y="95" width="26" height="9"/><rect x="111" y="95" width="26" height="7"/><rect x="155" y="94" width="26" height="9"/><circle cx="205" cy="99" r="6"/>
      <rect x="67" y="117" width="26" height="7"/><rect x="111" y="117" width="26" height="7"/><rect x="155" y="117" width="26" height="7"/><rect x="199" y="115" width="12" height="11"/>
    </g>
  </svg>
  <div class="footer"><span>© 2017 All rights reserved</span><span>02</span></div>
</section>

<!-- Our chart bars -->
<section class="slide c1 r4">
  <div class="brand brand-sm">QUARVEX</div>
  <div class="head"><h2>OUR CHART</h2><p>SUBTITLE GOES HERE</p></div>
  <div class="abs" style="left:22px;top:51px;width:150px">
    <p style="font-size:3.2px;font-weight:600;margin-bottom:1px">Lorem ipsum dolor sit amet</p>
    <p class="body" style="margin-bottom:4px">consectetur adipiscing elit, sed do eiusmod tempor incididunt ut labore et dolore magna aliqua. Ut enim ad minim veniam, quis nostrud exercitation ullamco laboris nisi ut aliquip ex ea commodo consequat. Duis aute irure dolor in reprehenderit in voluptate velit esse cillum dolore eu fugiat nulla pariatur.</p>
    <p style="font-size:3.2px;font-weight:600;margin-bottom:1px">Lorem ipsum dolor sit amet</p>
    <p class="body" style="margin-bottom:4px">consectetur adipiscing elit, sed do eiusmod tempor incididunt ut labore et dolore magna aliqua. Ut enim ad minim veniam, quis nostrud exercitation ullamco laboris nisi ut aliquip ex ea commodo consequat. Duis aute irure dolor in reprehenderit in voluptate velit esse cillum dolore eu.</p>
    <p style="font-size:3.2px;font-weight:600;margin-bottom:1px">Lorem ipsum dolor sit amet</p>
    <p class="body">Excepteur sint occaecat cupidatat non proident, sunt in culpa qui officia deserunt mollit anim id est laborum. Excepteur sint occaecat cupidatat non.</p>
  </div>
  <svg class="abs" style="left:0;top:0" width="289" height="162" font-family="Inter,sans-serif">
    <path d="M185 37v50h82" fill="none" stroke="#2a2f45" stroke-width="0.5"/>
    <g fill="#2b3963"><rect x="189" y="58" width="3.5" height="29"/><rect x="207" y="61" width="3.5" height="26"/><rect x="225" y="57" width="3.5" height="30"/><rect x="243" y="54" width="3.5" height="33"/></g>
    <g fill="#8a8b8f"><rect x="194" y="66" width="3.5" height="21"/><rect x="212" y="50" width="3.5" height="37"/><rect x="230" y="69" width="3.5" height="18"/><rect x="248" y="64" width="3.5" height="23"/></g>
    <g fill="#4a4f62"><rect x="199" y="71" width="3.5" height="16"/><rect x="217" y="69" width="3.5" height="18"/><rect x="235" y="62" width="3.5" height="25"/><rect x="253" y="57" width="3.5" height="30"/></g>
    <rect x="210" y="44" width="7" height="3" fill="#8a8b8f"/><rect x="252" y="48" width="7" height="3" fill="#2b3963"/>
    <g font-size="2.6" fill="#444" text-anchor="middle"><text x="196" y="92">2009</text><text x="214" y="92">2010</text><text x="232" y="92">2011</text><text x="250" y="92">2012</text></g>
    <g font-size="2.6" fill="#2a2f45">
      <rect x="197" y="103" width="2.5" height="2.5" fill="#2b3963"/><text x="202" y="105.5" font-weight="600">LOREM IPSUM</text>
      <text x="202" y="109" fill="#666">Lorem ipsum dolor sit amet consectetur</text><text x="202" y="112" fill="#666">adipiscing elit, sed do eiusmod tempor</text>
      <rect x="197" y="120" width="2.5" height="2.5" fill="#8a8b8f"/><text x="202" y="122.5" font-weight="600">LOREM IPSUM</text>
      <text x="202" y="126" fill="#666">Lorem ipsum dolor sit amet consectetur</text><text x="202" y="129" fill="#666">adipiscing elit, sed do eiusmod tempor</text>
      <rect x="197" y="137" width="2.5" height="2.5" fill="#4a4f62"/><text x="202" y="139.5" font-weight="600">LOREM IPSUM</text>
    </g>
  </svg>
  <div class="footer"><span>© 2017 All rights reserved</span><span>02</span></div>
</section>

<!-- Our chart donuts -->
<section class="slide c2 r4">
  <div class="brand brand-sm">QUARVEX</div>
  <div class="head"><h2>OUR CHART</h2><p>SUBTITLE GOES HERE</p></div>
  <svg class="abs" style="left:0;top:0" width="289" height="162" font-family="Inter,sans-serif">
    <g fill="none" stroke-width="3.5">
      <circle cx="68" cy="71" r="16" stroke="#8a8b8f"/><circle cx="68" cy="71" r="16" stroke="#2b3963" stroke-dasharray="81.4 100.5" transform="rotate(-90 68 71)"/>
      <circle cx="153" cy="71" r="16" stroke="#8a8b8f"/><circle cx="153" cy="71" r="16" stroke="#2b3963" stroke-dasharray="72.4 100.5" transform="rotate(-90 153 71)"/>
      <circle cx="234" cy="71" r="16" stroke="#8a8b8f"/><circle cx="234" cy="71" r="16" stroke="#2b3963" stroke-dasharray="63.3 100.5" transform="rotate(-90 234 71)"/>
    </g>
    <g font-size="7" fill="#2b3963" font-weight="700" text-anchor="middle"><text x="68" y="73.5">81%</text><text x="153" y="73.5">72%</text><text x="234" y="73.5">63%</text></g>
  </svg>
  <p class="abs center" style="left:38px;top:98px;width:60px;font-size:2.9px;line-height:1.35;color:#444">dolor sit amet, consectetur adipisicing elit, sed do eiusmod tempor incididunt ut labore et dolore magna aliqua. Ut enim ad minim veniam, quis nostrud exercitation ullamco laboris nisi ut aliquip ex ea commodo consequat fugiat nulla pariatur.</p>
  <p class="abs center" style="left:123px;top:98px;width:60px;font-size:2.9px;line-height:1.35;color:#444">dolor sit amet, consectetur adipisicing elit, sed do eiusmod tempor incididunt ut labore et dolore magna aliqua. Ut enim ad minim veniam, quis nostrud exercitation ullamco laboris nisi ut aliquip ex ea commodo consequat fugiat nulla pariatur.</p>
  <p class="abs center" style="left:204px;top:98px;width:60px;font-size:2.9px;line-height:1.35;color:#444">dolor sit amet, consectetur adipisicing elit, sed do eiusmod tempor incididunt ut labore et dolore magna aliqua. Ut enim ad minim veniam, quis nostrud exercitation ullamco laboris nisi ut aliquip ex ea commodo consequat fugiat nulla pariatur.</p>
  <div class="footer"><span>© 2017 All rights reserved</span><span>02</span></div>
</section>

<!-- Our team -->
<section class="slide c3 r4">
  <div class="brand brand-sm">QUARVEX</div>
  <div class="head"><h2>OUR TEAM</h2><p>SUBTITLE GOES HERE</p></div>
  <svg class="abs" style="left:0;top:0" width="289" height="162">
    <g stroke="#2b3963" stroke-width="0.8">
      <circle cx="58" cy="61" r="14" fill="#c9cbd0" role="img" aria-label="Portrait of Jonathan Doe"/>
      <circle cx="145" cy="61" r="14" fill="#c9cbd0" role="img" aria-label="Portrait of Melanie Doe"/>
      <circle cx="236" cy="61" r="14" fill="#c9cbd0" role="img" aria-label="Portrait of Natalie Doe"/>
    </g>
  </svg>
  <div class="abs center" style="left:28px;top:82px;width:60px;font-size:3.2px;font-weight:600">JONATHAN DOE<br><span style="font-weight:400;font-style:italic;color:#666">president</span></div>
  <div class="abs center" style="left:115px;top:82px;width:60px;font-size:3.2px;font-weight:600">MELANIE DOE<br><span style="font-weight:400;font-style:italic;color:#666">vice president</span></div>
  <div class="abs center" style="left:206px;top:82px;width:60px;font-size:3.2px;font-weight:600">NATALIE DOE<br><span style="font-weight:400;font-style:italic;color:#666">vice president</span></div>
  <p class="abs center" style="left:28px;top:98px;width:60px;font-size:2.9px;line-height:1.35;color:#444">dolor sit amet, consectetur adipisicing elit, sed do eiusmod tempor incididunt ut labore et dolore magna aliqua. Ut enim ad minim veniam, quis nostrud exercitation ullamco laboris nisi ut aliquip ex ea commodo fugiat nulla pariatur.</p>
  <p class="abs center" style="left:115px;top:98px;width:60px;font-size:2.9px;line-height:1.35;color:#444">dolor sit amet, consectetur adipisicing elit, sed do eiusmod tempor incididunt ut labore et dolore magna aliqua. Ut enim ad minim veniam, quis nostrud exercitation ullamco laboris nisi ut aliquip ex ea commodo fugiat nulla pariatur.</p>
  <p class="abs center" style="left:206px;top:98px;width:60px;font-size:2.9px;line-height:1.35;color:#444">dolor sit amet, consectetur adipisicing elit, sed do eiusmod tempor incididunt ut labore et dolore magna aliqua. Ut enim ad minim veniam, quis nostrud exercitation ullamco laboris nisi ut aliquip ex ea commodo fugiat nulla pariatur.</p>
  <div class="footer"><span>© 2017 All rights reserved</span><span>02</span></div>
</section>

<!-- Our services split -->
<section class="slide c1 r5 on-dark">
  <div class="abs" style="left:0;top:0;width:124px;height:162px;background:var(--navy)"></div>
  <div class="photo" role="img" aria-label="Black and white photo of a smiling team" style="left:124px;top:0;width:165px;height:162px;background:linear-gradient(90deg,#f2f2f2,#b9b9b9 45%,#6f6f6f 75%,#d8d8d8)"></div>
  <div class="head"><h2>OUR SERVICES</h2><p>SUBTITLE GOES HERE</p></div>
  <p class="abs body light" style="left:18px;top:65px;width:96px;font-weight:600">Lorem ipsum dolor sit amet, consectetur adipisicing elit, sed do eiusmod tempor incididunt ut labore et dolore magna aliqua. Ut enim ad minim veniam, quis nostrud exercitation ullamco laboris nisi ut aliquip ex ea commodo consequat. Duis aute irure dolor in reprehenderit in voluptate velit esse cillum dolore eu fugiat nulla pariatur.</p>
  <div class="abs" style="left:4px;top:149px;font-size:5px;font-weight:700;color:var(--white)">Norvane</div>
</section>

<!-- Section title -->
<section class="slide c2 r5 on-dark">
  <div class="bg-photo" role="img" aria-label="Navy toned photo of a team meeting" style="background:linear-gradient(120deg,#3a4872,#54628c 50%,#36446e)"></div>
  <svg class="abs" style="left:0;top:0" width="289" height="162" font-family="Georgia,serif">
    <circle cx="145" cy="79" r="16" fill="#fff"/>
    <text x="145" y="87" text-anchor="middle" font-size="22" font-style="italic" font-weight="700" fill="#2b3963">i</text>
  </svg>
  <div class="abs center" style="left:0;top:110px;width:289px;font-size:7px;color:var(--white);letter-spacing:-0.2px">SECTION TITLE</div>
</section>

<!-- Thank you -->
<section class="slide c3 r5">
  <div class="brand brand-lg">QUARVEX</div>
  <div class="abs" style="left:25px;top:38px;height:19px;border-left:0.8px solid var(--ink)"></div>
  <div class="abs" style="left:31px;top:42px;font-size:6.5px;letter-spacing:-0.2px">THANK YOU</div>
  <div class="abs" style="left:31px;top:49px;font-size:7px;color:var(--muted);font-weight:300">FOR YOUR TIME</div>
  <div class="photo" role="img" aria-label="Map of the office location" style="left:0;top:63px;width:289px;height:74px;background:var(--map-fill)"></div>
  <svg class="abs" style="left:0;top:0" width="289" height="162">
    <g fill="#2b3963"><circle cx="28" cy="148" r="2.2"/><circle cx="120" cy="148" r="2.2"/><circle cx="210" cy="148" r="2.2"/></g>
    <rect x="0" y="157" width="289" height="5" fill="#2b3963"/>
  </svg>
  <div class="abs" style="left:33px;top:146.5px;font-size:3.2px">418 Harbor Point Ave Ste 120</div>
  <div class="abs" style="left:125px;top:146.5px;font-size:3.2px">support@quarvex.net</div>
  <div class="abs" style="left:215px;top:146.5px;font-size:3.2px">www.quarvex.net</div>
</section>

</div>
</body>
</html>
```